Create the ONLY Supplement line for Male Entrepreneurs! (Veltro Prime MD)

I need a label designed for a new supplement brand that I am launching.

There are five products so need a design that I can simply change the wording for each individual product

The brand name is called veltro prime MD. The focus is male entrepreneurial health.

Target audience is men 35 to 55.

Concepts: the healthier you are in body the more money you will make in business.

Concept to copy: I want to make a clean minimalistic label mimicking Dallamore MD (google it and you'll see what I mean)

Target Market(s)

male entrepreneurs 35-55

Industry/Entity Type

Health Supplement

Colors

Designer to choose colors to be used in the design.

Requirements
Must have
• Modern classy design, similar to Dallamore MD.
Nice to have
• Highlight that the supplement is Doctor Approved.
Should not have
• No loud colors. Present it as high class.

```html
<!DOCTYPE html>
<html lang="en">
<head>
<meta charset="utf-8">
<title>Veltro Prime MD — Health Supplement Label</title>
<link href="https://fonts.googleapis.com/css2?family=Cabin:wght@400;500&display=swap" rel="stylesheet">
<style>
  :root {
    --paper: #ffffff;
    --brand-red: #cc1f24;
    --blush: #fdd3e8;
    --blush-line: #fbd0e4;
    --blush-faint: #fde6f1;
    --blush-text: #f8c4dd;
  }
  * { box-sizing: border-box; margin: 0; padding: 0; }
  html, body { width: 1200px; height: 1000px; overflow: hidden; background: var(--paper); }
  body { font-family: "Cabin", "Gill Sans", sans-serif; color: var(--brand-red); }

  .label-sheet { position: relative; width: 1200px; height: 1000px; }

  .label-frame {
    position: absolute; left: 83px; top: 297px; width: 1025px; height: 405px;
    border: 1.5px solid var(--blush-faint);
  }
  .panel-divider { position: absolute; top: 297px; height: 405px; width: 2px; background: var(--blush-line); }
  .panel-divider--outer { left: 441px; width: 1px; background: var(--blush-faint); }
  .panel-divider--inner { left: 448px; width: 3px; }

  .base-rule { position: absolute; left: 83px; width: 1025px; top: 675px; height: 4px; background: var(--blush-line); }

  .registration-cross { position: absolute; left: 424px; top: 652px; }

  .side-tab { position: absolute; left: 83px; width: 34px; height: 68px; background: var(--blush); }
  .side-tab--one { top: 370px; }
  .side-tab--two { top: 466px; }
  .side-tab--three { top: 562px; }

  .colour-chip { position: absolute; width: 37px; background: var(--blush); }
  .colour-chip--top { top: 298px; height: 23px; }
  .colour-chip--bottom { top: 637px; height: 64px; }
  .chip-a { left: 935px; }
  .chip-b { left: 987px; }
  .chip-c { left: 1040px; }

  .fine-print {
    position: absolute; font-size: 5.6px; line-height: 8.1px; text-align: justify;
    color: var(--brand-red); font-weight: 500;
  }
  .fine-print--usage { left: 132px; top: 378px; width: 246px; }
  .fine-print--warning { left: 131px; top: 475px; width: 246px; }
  .fine-print--ingredients { left: 135px; top: 571px; width: 244px; }
  .fine-print--story { left: 860px; top: 362px; width: 219px; font-size: 5.7px; line-height: 8.8px; }
  .fine-print--story p { margin-bottom: 1px; }

  .brand-spine {
    position: absolute; left: 456px; top: 322px;
    writing-mode: vertical-rl; font-size: 22px; letter-spacing: 0.2px; white-space: nowrap;
  }

  .brand-mark {
    position: absolute; left: 540px; top: 500px; width: 200px; text-align: center;
    font-size: 11px; letter-spacing: 0.5px;
  }

  .product-title { position: absolute; left: 540px; top: 539px; width: 200px; text-align: center; font-size: 20.5px; }
  .product-meta { position: absolute; left: 540px; width: 200px; text-align: center; font-size: 13.5px; }
  .product-meta--type { top: 578px; }
  .product-meta--count { top: 605px; }
  .title-rule { position: absolute; left: 547px; width: 191px; height: 1.5px; background: var(--blush-line); }
  .title-rule--one { top: 569px; }
  .title-rule--two { top: 600px; }
  .title-rule--three { top: 627px; }

  .doctor-approved {
    position: absolute; left: 457px; top: 651px; font-size: 17px; letter-spacing: 0.2px; color: var(--blush-text);
  }
</style>
</head>
<body>
<main class="label-sheet">
  <div class="label-frame"></div>
  <div class="panel-divider panel-divider--outer"></div>
  <div class="panel-divider panel-divider--inner"></div>
  <div class="base-rule"></div>

  <div class="side-tab side-tab--one"></div>
  <div class="side-tab side-tab--two"></div>
  <div class="side-tab side-tab--three"></div>

  <div class="colour-chip colour-chip--top chip-a"></div>
  <div class="colour-chip colour-chip--top chip-b"></div>
  <div class="colour-chip colour-chip--top chip-c"></div>
  <div class="colour-chip colour-chip--bottom chip-a"></div>
  <div class="colour-chip colour-chip--bottom chip-b"></div>
  <div class="colour-chip colour-chip--bottom chip-c"></div>

  <p class="fine-print fine-print--usage">Formulated for men who lead. Each capsule blends key vitamins, minerals and botanical extracts chosen to support steady energy, clear focus and a strong heart through long working days. Take two capsules daily with food and a full glass of water. Do not exceed the stated dose. Consult your doctor before use if you take medication or have a medical condition. Store in a cool dry place.</p>
  <p class="fine-print fine-print--warning">Keep out of reach of children. Not intended to diagnose, treat, cure or prevent any disease. Do not use if the safety seal under the cap is broken or missing. Manufactured in a certified facility.</p>
  <p class="fine-print fine-print--ingredients">Ingredients: vitamin D3, zinc, magnesium, ashwagandha root extract, rhodiola, green tea leaf extract, coenzyme Q10, vegetable cellulose capsule. Free from gluten, dairy, soy and artificial colours. Best taken in the morning to support energy and recovery across a demanding schedule. Results may vary by person.</p>

  <h2 class="brand-spine">Veltro prime MD</h2>

  <p class="brand-mark">Veltro Prime MD</p>
  <h1 class="product-title">Health Supplement</h1>
  <div class="title-rule title-rule--one"></div>
  <p class="product-meta product-meta--type">Dietry Suppliment</p>
  <div class="title-rule title-rule--two"></div>
  <p class="product-meta product-meta--count">90 Capsules</p>
  <div class="title-rule title-rule--three"></div>

  <p class="doctor-approved">DOCTOR APPROVED</p>

  <svg class="registration-cross" width="50" height="50" viewBox="0 0 50 50" aria-hidden="true">
    <line x1="0" y1="25" x2="50" y2="25" stroke="var(--brand-red)" stroke-width="3.5"/>
    <line x1="25" y1="0" x2="25" y2="50" stroke="var(--brand-red)" stroke-width="3.5"/>
  </svg>

  <div class="fine-print fine-print--story">
    <p>Built for the man who runs the business. A sharper body supports a sharper mind, and a sharper mind makes better decisions. This daily formula was developed with physicians to help you keep pace with long hours, travel and pressure, so your health becomes an asset rather than a cost you pay later in life.</p>
    <p>Each serving delivers clinically studied nutrients in measured amounts. Magnesium and zinc help normal muscle function and testosterone levels. Vitamin D3 supports immunity and bone strength. Adaptogenic herbs help the body respond to stress while keeping you calm and focused.</p>
    <p>Green tea leaf and coenzyme Q10 support cellular energy and a healthy heart, giving steady drive through the afternoon without the crash that follows sugar or extra coffee. Every batch is tested for purity and strength by an independent laboratory before it leaves our facility.</p>
    <p>Directions: take two capsules each morning with breakfast. For best results use daily for at least eight weeks alongside regular exercise, good sleep and a balanced diet. Pair with the rest of the range to build a complete routine for body and mind.</p>
    <p>Doctor approved and made to a high standard. Contains no fillers, binders or artificial flavours. Suitable for vegetarians. If you are under medical supervision, speak with your physician before starting any new supplement. Your health is your most valuable investment.</p>
  </div>
</main>
</body>
</html>
```